business cards, stationary
lets see what you got
Use specific fonts
up to designer
Modern
Calvin Marsh
Director of Sales
1870 Quarrymill road, Suite 114 Burlington, On L4K 3P8
Calvin@sunlanejourneys.example
www.sunlanejourneys.example
BBM: 58720936
LOGO on back

```html
<!DOCTYPE html>
<html lang="en">
<head>
<meta charset="utf-8">
<title>Sun Lane Journeys – Stationery</title>
<link href="https://fonts.googleapis.com/css2?family=Arimo:wght@400;700&display=swap" rel="stylesheet">
<style>
:root{
  --bg:#353535;
  --bg-light:#4a4a4a;
  --green:#7cbb2a;
  --green-dark:#5e9a17;
  --purple:#5a2b78;
  --paper:#ffffff;
  --ink:#555555;
  --ink-light:#9a9a9a;
  --label:#bdbdbd;
}
*{box-sizing:border-box;margin:0;padding:0}
html,body{width:1200px;height:338px;overflow:hidden}
body{
  background:radial-gradient(ellipse at 50% 45%,var(--bg-light),var(--bg) 75%);
  font-family:"Arimo",Arial,sans-serif;color:var(--ink);position:relative;
}
.abs{position:absolute}
.label{position:absolute;font-size:7px;color:var(--label);text-align:center}
.brand{display:flex;align-items:center;gap:5px;color:var(--green);font-weight:700;white-space:nowrap}
.brand .dot{border-radius:50%;background:var(--green);flex:none}
.brand.light{color:#fff}
.brand.light .dot{background:#fff}

/* hero logo */
.hero{left:16px;top:44px;font-size:19px}
.hero .dot{width:16px;height:16px}

/* cards */
.card{position:absolute;width:122px;height:70px;overflow:hidden;box-shadow:0 1px 3px rgba(0,0,0,.5)}
.card.white{background:var(--paper)}
.card.green{background:var(--green)}
.card.purple{background:var(--purple)}
.card svg.swoosh{position:absolute;left:0;bottom:0;width:100%;height:22px}
.card.white svg.swoosh{height:13px}
.card .brand{position:absolute;left:7px;top:7px;font-size:7px}
.card .brand .dot{width:6px;height:6px}
.card .who{position:absolute;right:7px;top:17px;text-align:right;font-size:4.4px;line-height:1.3;color:var(--ink);white-space:nowrap}
.card .who b{display:block;font-size:5.6px;line-height:1.2;color:var(--green-dark);margin-bottom:0.5px}
.card .center{position:absolute;left:0;right:0;top:28px;display:flex;justify-content:center;font-size:8px}
.card .center .dot{width:7px;height:7px}

/* letterheads */
.sheet{position:absolute;top:18px;width:170px;height:266px;background:var(--paper);overflow:hidden;box-shadow:0 1px 4px rgba(0,0,0,.5)}
.sheet .brand{position:absolute;left:12px;top:12px;font-size:8px}
.sheet .brand .dot{width:7px;height:7px}
.letter{position:absolute;left:12px;right:14px;top:36px;font-size:3.4px;line-height:1.5;color:var(--ink)}
.letter p{margin-bottom:3.5px}
.sheet .foot{position:absolute;right:10px;bottom:8px;font-size:3.3px;line-height:1.45;text-align:right;color:var(--ink-light);width:80px}
.sheet svg.wave{position:absolute;left:0;bottom:0;width:100%;height:42px}

.fax{position:absolute;left:12px;right:12px;top:36px;font-size:3.6px;color:var(--ink)}
.fax table{width:100%;border-collapse:collapse}
.fax td{border-bottom:0.5px solid #bbb;height:9px;vertical-align:bottom;padding-bottom:1px}
.fax .checks{display:flex;gap:5px;margin-top:6px;border-bottom:0.5px solid #bbb;padding-bottom:2px}
.fax .checks span::before{content:"";display:inline-block;width:3px;height:3px;border:0.4px solid #888;margin-right:1.5px;vertical-align:-0.5px}
.fax .comments{margin-top:6px;font-weight:700;font-size:4px}
.fax .faint{position:absolute;left:40px;top:52px;width:70px;height:70px;border-radius:50%;background:radial-gradient(circle,rgba(124,187,42,.14),rgba(124,187,42,0) 70%)}

/* envelopes */
.env{position:absolute;width:152px;height:66px;overflow:hidden;box-shadow:0 1px 3px rgba(0,0,0,.5)}
.env.white{background:var(--paper)}
.env.purple{background:var(--purple)}
.env.green{background:var(--green)}
.env .brand{position:absolute;left:8px;top:8px;font-size:7px}
.env .brand .dot{width:6px;height:6px}
.env .center{position:absolute;left:0;right:0;bottom:12px;display:flex;justify-content:center;font-size:8px}
.env .center .dot{width:7px;height:7px}
.env svg{position:absolute;left:0;width:100%}
.env .addr{position:absolute;left:8px;top:18px;font-size:3.3px;line-height:1.4;color:var(--ink-light)}
</style>
</head>
<body>

<!-- identity column -->
<div class="brand hero abs"><span class="dot"></span>sunlanejourneys.example</div>
<div class="label" style="left:49px;top:104px;width:40px">front</div>
<div class="label" style="left:181px;top:104px;width:40px">back</div>

<div class="card white" style="left:8px;top:118px">
  <div class="brand"><span class="dot"></span>sunlanejourneys</div>
  <div class="who">
    <b>Calvin Marsh</b>Director of Sales<br>1870 Quarrymill road, Suite 114<br>Burlington, On L4K 3P8<br>Calvin@sunlanejourneys.example<br>www.sunlanejourneys.example<br>BBM: 58720936
  </div>
  <svg class="swoosh" viewBox="0 0 122 22" preserveAspectRatio="none"><path d="M0 10 C30 22 70 2 122 14 V22 H0Z" fill="var(--green)"/><path d="M0 16 C35 24 80 10 122 19 V22 H0Z" fill="var(--purple)"/></svg>
</div>
<div class="card green" style="left:140px;top:118px">
  <div class="center brand light"><span class="dot"></span>sunlanejourneys.example</div>
  <svg class="swoosh" viewBox="0 0 122 22" preserveAspectRatio="none"><path d="M0 14 C40 4 80 24 122 10 V22 H0Z" fill="var(--green-dark)"/></svg>
</div>

<div class="card white" style="left:8px;top:196px">
  <div class="brand"><span class="dot"></span>sunlanejourneys</div>
  <div class="who">
    <b>Calvin Marsh</b>Director of Sales<br>1870 Quarrymill road, Suite 114<br>Burlington, On L4K 3P8<br>Calvin@sunlanejourneys.example<br>www.sunlanejourneys.example<br>BBM: 58720936
  </div>
  <svg class="swoosh" viewBox="0 0 122 22" preserveAspectRatio="none"><path d="M0 12 C40 22 80 4 122 12 V22 H0Z" fill="var(--purple)"/></svg>
</div>
<div class="card purple" style="left:140px;top:196px">
  <div class="center brand light"><span class="dot"></span>sunlanejourneys.example</div>
  <svg class="swoosh" viewBox="0 0 122 22" preserveAspectRatio="none"><path d="M0 14 C40 4 80 24 122 10 V22 H0Z" fill="var(--green)"/></svg>
</div>
<div class="label" style="left:49px;top:272px;width:40px">front</div>
<div class="label" style="left:181px;top:272px;width:40px">back</div>

<!-- letterhead option 1 -->
<div class="sheet" style="left:312px">
  <div class="brand"><span class="dot"></span>sunlanejourneys.example</div>
  <div class="letter">
    <p>June 3, 2024</p>
    <p>Client Name<br>Street Address<br>City, Province</p>
    <p>Dear Client,</p>
    <p>Thank you for choosing our team for your next getaway. We look forward to planning every detail with care.</p>
    <p>Our agents will contact you shortly with options, dates and pricing that suit your group and budget.</p>
    <p>Please reach out at any time with questions.</p>
    <p>Sincerely,<br><br>Calvin Marsh</p>
  </div>
  <svg class="wave" viewBox="0 0 170 42" preserveAspectRatio="none"><path d="M0 8 C40 30 70 34 110 42 H0Z" fill="var(--green)"/><path d="M0 24 C30 36 50 40 70 42 H0Z" fill="var(--purple)"/></svg>
  <div class="foot">1870 Quarrymill road, Suite 114<br>Burlington, On L4K 3P8<br>Calvin@sunlanejourneys.example<br>www.sunlanejourneys.example</div>
</div>
<div class="label" style="left:312px;top:290px;width:170px">letterhead option 1</div>

<!-- letterhead option 2 / fax -->
<div class="sheet" style="left:494px">
  <div class="brand"><span class="dot"></span>sunlanejourneys.example</div>
  <div class="fax">
    <div class="faint" role="img" aria-label="Faint brand decoration"></div>
    <table>
      <tr><td>To:</td><td>From:</td></tr>
      <tr><td>Fax:</td><td>Pages:</td></tr>
      <tr><td>Phone:</td><td>Date:</td></tr>
      <tr><td>Re:</td><td>CC:</td></tr>
    </table>
    <div class="checks"><span>Urgent</span><span>For Review</span><span>Please Comment</span><span>Please Reply</span><span>Please Recycle</span></div>
    <div class="comments">COMMENTS:</div>
  </div>
  <svg class="wave" viewBox="0 0 170 42" preserveAspectRatio="none"><path d="M0 8 C40 30 70 34 110 42 H0Z" fill="var(--green)"/><path d="M0 24 C30 36 50 40 70 42 H0Z" fill="var(--purple)"/></svg>
  <div class="foot">1870 Quarrymill road, Suite 114<br>Burlington, On L4K 3P8<br>Calvin@sunlanejourneys.example<br>www.sunlanejourneys.example</div>
</div>
<div class="label" style="left:494px;top:290px;width:170px">letterhead option 2</div>

<!-- envelopes column A -->
<div class="env white" style="left:680px;top:22px">
  <div class="brand"><span class="dot"></span>sunlanejourneys</div>
  <div class="addr">1870 Quarrymill road, Suite 114<br>Burlington, On L4K 3P8</div>
  <svg viewBox="0 0 152 20" preserveAspectRatio="none" style="bottom:0;height:20px"><path d="M0 6 C50 22 100 0 152 12 V20 H0Z" fill="var(--green)"/><path d="M0 14 C50 22 110 10 152 17 V20 H0Z" fill="var(--purple)"/></svg>
</div>
<div class="label" style="left:680px;top:94px;width:152px">envelope option 1</div>

<div class="env white" style="left:680px;top:122px">
  <div class="brand"><span class="dot"></span>sunlanejourneys</div>
  <div class="addr">1870 Quarrymill road, Suite 114<br>Burlington, On L4K 3P8</div>
  <svg viewBox="0 0 152 20" preserveAspectRatio="none" style="bottom:0;height:20px"><path d="M0 10 C50 20 100 2 152 10 V20 H0Z" fill="var(--purple)"/></svg>
</div>
<div class="label" style="left:680px;top:194px;width:152px">envelope option 2</div>

<div class="env white" style="left:680px;top:222px">
  <div class="brand"><span class="dot"></span>sunlanejourneys</div>
  <div class="addr">1870 Quarrymill road, Suite 114<br>Burlington, On L4K 3P8</div>
  <svg viewBox="0 0 152 20" preserveAspectRatio="none" style="bottom:0;height:20px"><path d="M0 10 C50 20 100 2 152 10 V20 H0Z" fill="var(--green)"/></svg>
</div>
<div class="label" style="left:680px;top:294px;width:152px">envelope option 3</div>

<!-- envelopes column B (backs) -->
<div class="env white" style="left:1030px;top:22px">
  <svg viewBox="0 0 152 66" preserveAspectRatio="none" style="top:0;height:66px"><path d="M0 0 L76 30 L152 0" fill="none" stroke="#ddd" stroke-width="1"/><path d="M0 56 C50 70 100 46 152 58 V66 H0Z" fill="var(--green)"/></svg>
</div>
<div class="label" style="left:1030px;top:94px;width:152px">envelope option 1</div>

<div class="env purple" style="left:1030px;top:122px">
  <svg viewBox="0 0 152 66" preserveAspectRatio="none" style="top:0;height:66px"><path d="M0 0 L76 26 L152 0Z" fill="#4a2164"/></svg>
  <div class="center brand light"><span class="dot"></span>sunlanejourneys.example</div>
</div>
<div class="label" style="left:1030px;top:194px;width:152px">envelope option 2</div>

<div class="env green" style="left:1030px;top:222px">
  <svg viewBox="0 0 152 66" preserveAspectRatio="none" style="top:0;height:66px"><path d="M0 0 L76 26 L152 0Z" fill="var(--green-dark)"/></svg>
  <div class="center brand light"><span class="dot"></span>sunlanejourneys.example</div>
</div>
<div class="label" style="left:1030px;top:294px;width:152px">envelope option 3</div>

</body>
</html>
```